Visitenkarten-Design für Lichtfeder - Zeilen von Hand zu Hand
Zielgruppe
Ich schreibe Briefe an Menschen, die mehr über sich erfahren wollen, die sich berühren lassen wollen, die an sich arbeiten möchten, die sich entfalten wollen. Ich möchte nicht den Verstand sondern das Herz ansprechen, die Selbstheilung erfahren möchten, damit sie Impulse bekommen, um ein glücklicheres Leben zu führen, das ihnen mehr entspricht.
Ich sehe mich als Mensch, der andere Menschen in ihrem Leben unterstützen möchte.
Aufgabenstellung
Die Briefe schreibe ich in Segoe Print, goldene Schrift auf gelblichem Papier, evtl auch anderes Papier, wenn die goldene Schrift passt.
Die Visitenkarte sollte Freude, Freiheit und Anerkennung des Menschen an sich ausstrahlen. Farben evtl. Bordeaux, mit vielleicht Rosa. Sie sollte jedoch nicht kitschig wirken.
Schön wäre vielleicht etwas mit Blumen oder Ornamenten, jedoch nicht zu überladen.
Als Text soll drauf sein:
Das beigefügte Logo, dann:
Berühren - Bewegen - Begeistern

```html
<!DOCTYPE html>
<html lang="de">
<head>
<meta charset="utf-8">
<title>Lichtfeder – Visitenkarte</title>
<link rel="stylesheet" href="https://fonts.googleapis.com/css2?family=Kalam:wght@400;700&family=Marcellus&display=swap">
<style>
  :root {
    --stage: #000000;
    --bordeaux: #921120;
    --wine: #6b1530;
    --gold: #e8b624;
    --gold-soft: #c59a3e;
    --paper: #ffffff;
  }
  * { margin: 0; padding: 0; box-sizing: border-box; }
  html, body { width: 908px; height: 1200px; overflow: hidden; background: var(--stage); }
  .sheet { position: relative; width: 908px; height: 1200px; background: var(--stage); }
  .card {
    position: absolute; left: 55px; width: 798px; height: 535px;
  }
  .card--front { top: 51px; background: var(--bordeaux); }
  .card--back { top: 613px; background: var(--paper); }

  .brand { position: absolute; left: 0; width: 100%; text-align: center; }
  .brand__name {
    font-family: "Kalam", cursive;
    font-weight: 400;
    font-size: 96px;
    line-height: 1;
    letter-spacing: 1px;
  }
  .brand__line {
    font-family: "Marcellus", serif;
    font-size: 17px;
    letter-spacing: 2px;
    margin-top: 6px;
  }
  .card--front .brand { top: 88px; }
  .card--front .brand__name { color: var(--gold); }
  .card--front .brand__line { color: var(--gold); }
  .card--back .brand { top: 92px; }
  .card--back .brand__name { color: var(--wine); }
  .card--back .brand__line { color: var(--wine); }

  .motto {
    position: absolute; top: 448px; left: 0; width: 100%; text-align: center;
    font-family: "Kalam", cursive; font-size: 25px; color: var(--gold);
    letter-spacing: 0.5px;
  }

  .contact {
    position: absolute; left: 460px; top: 305px; width: 300px; text-align: center;
    font-family: "Kalam", cursive; color: var(--gold-soft);
  }
  .contact__person {
    font-weight: 700; font-size: 26px; color: var(--wine); margin-bottom: 22px;
    letter-spacing: 0.5px;
  }
  .contact__item { font-size: 18px; line-height: 37px; letter-spacing: 0.5px; }
</style>
</head>
<body>
<main class="sheet">
  <section class="card card--front">
    <div class="brand">
      <p class="brand__name">Lichtfeder</p>
      <p class="brand__line">ZEILEN VON HAND ZU HAND</p>
    </div>
    <p class="motto">Berühren – Bewegen – Begeistern</p>
  </section>

  <section class="card card--back">
    <div class="brand">
      <p class="brand__name">Lichtfeder</p>
      <p class="brand__line">ZEILEN VON HAND ZU HAND</p>
    </div>
    <div class="contact">
      <p class="contact__person">Clara Brenner</p>
      <p class="contact__item">www.clarabrenner.de</p>
      <p class="contact__item">Mail: lichtfeder@postfach-mail.de</p>
      <p class="contact__item">Tel. +49 160 55 214 907</p>
    </div>
  </section>
</main>
</body>
</html>
```